Need new to-go sticker labels for my restaurant

I need to go sticker labels that are Modern, eye catching and sleek for sushi restaurant. Or it can be really nostalgic. Please include our logo somehow. It will be printed on a 1" x 2.65" label.

I need to also change each label name and price. Or can you tell me how to change each one or do I send you each label name and price?

Example:

California Roll.
Crab, Avocado, Cucumber
$8.99

Target Market(s)

Health conscious.

Industry/Entity Type

Restaurant

Requirements
Must have
• fresh food appeal. Nostalgia and warmth. Don't make it cookie cutter and just stick balun logo and sushi name, create a picture!! Create something very creative and infuse picture with logo.
Nice to have
• Warmth, nostalgia, fresh looking. Prefer warm tones with fresh appeal. Pick and choose Lime green, red, yellow are fine. Other colors can be used to make exciting!! must catch eye!!! Customers buy WITH THEIR EYES!!!
Should not have
• Should Not be cookie cutter and unnoticed.

```html
<!DOCTYPE html>
<html lang="en">
<head>
<meta charset="utf-8">
<title>Balun – To-go Label</title>
<link rel="stylesheet" href="https://fonts.googleapis.com/css2?family=Arimo:wght@700&family=Roboto+Condensed:wght@500&family=Montserrat:wght@700&display=swap">
<style>
  :root {
    --page: #ffffff;
    --label-dark: #221e16;
    --band-dark: #2e2920;
    --paper: #ffffff;
    --brand-red: #d4141c;
    --badge-red: #f21d0f;
    --badge-rim: #f0b48e;
    --ink: #0b0b0b;
    --ingredient: #f7d7bd;
    --gold: #c9a063;
    --flag-yellow: #fff35a;
    --art-light: #f4f1ec;
    --art-warm: #f3c9a8;
  }
  html, body {
    margin: 0;
    padding: 0;
    width: 1200px;
    height: 1000px;
    overflow: hidden;
    background: var(--page);
  }
  .canvas {
    position: relative;
    width: 1200px;
    height: 1000px;
    background: var(--page);
  }
  .label {
    position: absolute;
    left: 202px;
    top: 350px;
    width: 795px;
    height: 299px;
    overflow: hidden;
  }
  .label-shapes {
    position: absolute;
    inset: 0;
  }
  .brand {
    position: absolute;
    left: 110px;
    top: 214px;
    height: 42px;
    display: flex;
    align-items: center;
    gap: 10px;
    transform: rotate(-27deg);
    transform-origin: left center;
    z-index: 2;
  }
  .brand-mark {
    width: 16px;
    height: 16px;
    background: var(--brand-red);
  }
  .brand-name {
    font-family: "Montserrat", sans-serif;
    font-weight: 700;
    font-size: 42px;
    letter-spacing: 3px;
    color: var(--brand-red);
    line-height: 1;
  }
  .roll-art {
    position: absolute;
    left: 255px;
    top: 6px;
    width: 228px;
    height: 190px;
  }
  .menu-badge {
    position: absolute;
    left: 438px;
    top: 42px;
    width: 310px;
    height: 183px;
    text-align: center;
    font-family: "Arimo", sans-serif;
  }
  .dish-name {
    margin: 14px 0 0;
    font-weight: 700;
    font-size: 38px;
    line-height: 40px;
    color: var(--ink);
  }
  .ingredients {
    margin: 14px 0 0;
    font-family: "Roboto Condensed", sans-serif;
    font-weight: 500;
    font-size: 23px;
    color: var(--ingredient);
    display: flex;
    justify-content: center;
  }
  .ingredients span + span {
    border-left: 1.5px solid var(--ingredient);
    margin-left: 5px;
    padding-left: 5px;
  }
  .price-tag {
    position: absolute;
    left: 420px;
    top: 190px;
    width: 240px;
    height: 110px;
  }
  .price {
    position: absolute;
    left: 110px;
    top: 30px;
    font-family: "Arimo", sans-serif;
    font-weight: 700;
    font-size: 38px;
    color: var(--ink);
    transform: rotate(-3deg);
  }
  .currency {
    position: absolute;
    left: 20px;
    top: 9px;
    width: 78px;
    text-align: center;
    font-family: "Arimo", sans-serif;
    font-weight: 700;
    font-size: 54px;
    line-height: 78px;
    color: var(--paper);
  }
</style>
</head>
<body>
<div class="canvas">
  <section class="label">
    <svg class="label-shapes" width="795" height="299" viewBox="0 0 795 299">
      <rect width="795" height="299" fill="var(--label-dark)"/>
      <rect x="0" y="214" width="795" height="44" fill="var(--band-dark)" role="img" aria-label="Zigzag line pattern band"/>
      <polygon points="0,65 175,0 633,0 283,198 118,299" fill="var(--paper)"/>
      <path d="M438 30 H748 Q758 30 758 40 V225 Q758 237 745 237 H438 Q426 237 426 225 V40 Q426 30 438 30 Z" fill="var(--ink)"/>
      <rect x="437" y="40" width="311" height="185" rx="26" fill="var(--badge-rim)"/>
      <rect x="442" y="45" width="301" height="175" rx="22" fill="var(--badge-red)"/>
    </svg>

    <div class="brand">
      <div class="brand-mark"></div>
      <div class="brand-name">BALUN</div>
    </div>

    <svg class="roll-art" viewBox="0 0 228 190" role="img" aria-label="Illustration of sushi roll slices held by chopsticks">
      <defs>
        <radialGradient id="rollGlow" cx="50%" cy="50%" r="50%">
          <stop offset="0%" stop-color="var(--art-warm)"/>
          <stop offset="100%" stop-color="var(--art-light)"/>
        </radialGradient>
      </defs>
      <ellipse cx="120" cy="95" rx="105" ry="45" fill="url(#rollGlow)"/>
    </svg>

    <div class="menu-badge">
      <h1 class="dish-name">California<br>Roll</h1>
      <p class="ingredients"><span>Crab</span><span>Avocado</span><span>Cucumber</span></p>
    </div>

    <div class="price-tag">
      <svg width="240" height="110" viewBox="0 0 240 110">
        <path d="M88 20 Q150 8 232 4 L228 68 Q180 74 150 82 Q110 92 92 104 Z" fill="var(--flag-yellow)"/>
        <circle cx="59" cy="48" r="44" fill="var(--gold)" stroke="var(--gold)" stroke-width="3" stroke-dasharray="2 2"/>
        <circle cx="59" cy="48" r="38" fill="var(--gold)"/>
      </svg>
      <div class="currency">$</div>
      <div class="price">8.99</div>
    </div>
  </section>
</div>
</body>
</html>
```